Marketing Flyer for Plumber Referals

8.5" x11" Layout should be landscape not portrait. Create a bold, eye-catching flyer that highlights earning potential from referrals for water damage restoration. Use high-contrast colors like blue, yellow, and white, with bold fonts and dynamic layouts. Include images of restoration work, cash, and happy clients. Emphasize key benefits like $500 minimum payouts, fast payments, and unlimited income potential. Keep instructions simple: refer a client, we handle the work, you get paid. Add a clear call-to-action and display contact details prominently. Focus on professionalism and energy.

Target Market(s)

Plumbers and Contractor 8.5" x11" Layout should be landscape not portrait.

Industry/Entity Type

General Contractor

Colors
0054AA
0677BA
7BADD7
CADEEF
E8F1F8
EB3D1F
EC4F4E
F09395
F8D3D4
FCEDEE

Requirements
Must have
• 8.5" x11" Layout should be landscape not portrait.
Nice to have

```html
<!DOCTYPE html>
<html lang="en">
<head>
<meta charset="utf-8">
<title>Harborline Builders – Flood Referral Flyer</title>
<link href="https://fonts.googleapis.com/css2?family=Cinzel:wght@600;700&family=Montserrat:wght@400;500;600;700;800&display=swap" rel="stylesheet">
<style>
  :root{
    --red:#eb3d1f;
    --red-soft:#f09395;
    --ink:#111111;
    --black:#000000;
    --white:#ffffff;
    --grey-text:#555555;
    --bullet:#0054aa;
    --serif:"Cinzel", "Times New Roman", serif;
    --sans:"Montserrat", Arial, sans-serif;
  }
  *{box-sizing:border-box;margin:0;padding:0}
  html,body{width:1200px;height:498px;overflow:hidden;background:var(--white)}
  .sheet{position:relative;width:1200px;height:498px;background:var(--white)}
  .panel{position:absolute;top:39px;width:545px;height:421px;overflow:hidden;background:var(--black)}
  .panel--front{left:42px}
  .panel--back{left:619px}

  /* front */
  .flood-photo{position:absolute;left:0;top:0;width:545px;height:307px;
    background:linear-gradient(180deg,#6f6f6f 0%,#cfcfcf 22%,#e6e3de 40%,#8d8d8d 58%,#4a4a4a 75%,#9a9a9a 90%,#3c3c3c 100%)}
  .hero-banner{position:absolute;left:0;top:0;width:545px;height:200px}
  .headline{position:absolute;left:12px;font-family:var(--serif);font-weight:700;color:var(--ink);font-size:15.5px;letter-spacing:.2px;white-space:nowrap}
  .headline--one{top:47px}
  .headline--two{top:72px}
  .offer{position:absolute;left:12px;top:100px;color:var(--white);font-family:var(--sans)}
  .offer__big{font-weight:800;font-size:15px;letter-spacing:.5px;line-height:17px;margin-top:4px}
  .offer__small{font-weight:500;font-size:9.5px;line-height:13px;margin-top:2px}
  .partner-line{position:absolute;left:13px;top:147px;font-family:var(--sans);font-size:8.5px;color:#333}
  .tab-text{position:absolute;font-family:var(--serif);font-weight:700;color:var(--white);font-size:12.5px;white-space:nowrap}
  .tab-text--why{right:20px;top:282px}
  .tab-text--call{left:6px;top:282px}

  .info-band{position:absolute;left:0;top:307px;width:545px;height:114px;background:var(--black)}
  .divider{position:absolute;top:14px;width:1px;height:82px;background:#bbb}
  .brand{position:absolute;font-family:var(--serif);font-weight:600;color:var(--white);font-size:12.5px;text-align:center;line-height:16px;letter-spacing:.8px}
  .brand__mark{display:block;width:10px;height:10px;border:1px solid var(--white);margin:0 auto 8px}
  .benefits{position:absolute;left:196px;top:21px;list-style:none;font-family:var(--sans);font-size:7.9px;color:var(--white)}
  .benefits li{position:relative;padding-left:14px;height:15.7px;white-space:nowrap}
  .benefits li::before{content:"";position:absolute;left:0;top:2px;width:6px;height:6px;border-radius:50%;background:var(--bullet)}
  .benefits strong{font-weight:700}
  .slogan{position:absolute;right:20px;top:91px;font-family:var(--serif);font-weight:700;font-size:10px;color:var(--white)}

  /* back */
  .skyline-photo{position:absolute;left:0;top:0;width:545px;height:307px;
    background:linear-gradient(180deg,#8f7fc6 0%,#a48ad0 30%,#c49ac8 48%,#e7b6b8 58%,#4b3f66 66%,#c98a5a 74%,#5a4b7c 82%,#6f6396 100%)}
  .back-title{position:absolute;left:0;width:545px;text-align:center;font-family:var(--serif);font-weight:700;color:var(--white)}
  .back-title--main{top:17px;font-size:22px}
  .back-title--sub{top:48px;font-size:18px}
  .step{position:absolute;top:110px;width:146px;height:88px;background:var(--white);border-radius:12px;text-align:center;font-family:var(--sans)}
  .step--one{left:35px}.step--two{left:200px}.step--three{left:364px}
  .step__icon{position:absolute;left:50%;top:-23px;transform:translateX(-50%);width:46px;height:46px}
  .step__title{margin-top:31px;font-weight:700;font-size:7.8px;line-height:12px;color:var(--ink);letter-spacing:.3px}
  .step__body{margin-top:4px;font-size:8px;line-height:12px;color:var(--grey-text);padding:0 6px}
  .contact{position:absolute;left:60px;font-family:var(--sans);font-weight:700;color:var(--white);font-size:22px;white-space:nowrap}
  .contact--phone{top:19px}
  .contact--web{top:59px}
  .contact-icon{position:absolute;left:24px}
</style>
</head>
<body>
<div class="sheet">

  <!-- front side -->
  <section class="panel panel--front">
    <div class="flood-photo" role="img" aria-label="Photo of a flooded staircase hallway with water reflecting the steps"></div>
    <svg class="hero-banner" viewBox="0 0 545 200" aria-hidden="true">
      <polygon points="0,30 233,30 279,115 230,176 0,176" fill="#ffffff"/>
      <polyline points="0,29 234,29 280,115" fill="none" stroke="#eb3d1f" stroke-width="2.5"/>
      <polygon points="0,100 170,100 176,119 170,138 0,138" fill="#eb3d1f"/>
      <polyline points="172,100 178,100 184,119 178,138 172,138" fill="none" stroke="#888" stroke-width=".8"/>
    </svg>
    <div class="headline headline--one">EARN UNLIMITED CASH</div>
    <div class="headline headline--two">GET PAID TO REFER A FLOOD</div>
    <div class="offer">
      <div class="offer__big">$500 MINIMUM OR</div>
      <div class="offer__small">10% PER REFERRAL!</div>
    </div>
    <div class="partner-line">Partner with the #1 Water Damage Restoration Team</div>

    <svg style="position:absolute;left:0;top:264px" width="545" height="44" viewBox="0 0 545 44" aria-hidden="true">
      <polygon points="316,0 545,0 545,44 300,44" fill="#000"/>
      <polygon points="344,8 545,8 545,44 318,44" fill="#eb3d1f"/>
    </svg>
    <div class="tab-text tab-text--why">WHY PARTNER WITH US?</div>

    <div class="info-band">
      <div class="brand" style="left:0;width:173px;top:34px">
        <span class="brand__mark"></span>HARBORLINE<br>BUILDERS
      </div>
      <div class="divider" style="left:173px"></div>
      <ul class="benefits">
        <li><strong>Guaranteed Payout:</strong> Minimum $500 or 10% of the invoice, paid fast.</li>
        <li><strong>Free Evaluations:</strong> We assess damage and process insurance claims for your clients.</li>
        <li><strong>Industry Leaders:</strong> Certified experts with 24/7 rapid response.</li>
        <li><strong>Affordable Solutions:</strong> Lowest out-of-pocket costs for your customers.</li>
      </ul>
      <div class="slogan">Send Referrals. Get Paid. Grow Your Business.</div>
    </div>
  </section>

  <!-- back side -->
  <section class="panel panel--back">
    <div class="skyline-photo" role="img" aria-label="Photo of a waterfront city skyline at dusk under a purple sky"></div>
    <div class="back-title back-title--main">GET PAID TO REFER A FLOOD</div>
    <div class="back-title back-title--sub">HOW IT WORKS</div>

    <div class="step step--one">
      <svg class="step__icon" viewBox="0 0 46 46" aria-hidden="true">
        <circle cx="23" cy="23" r="23" fill="#f8d3d4" opacity=".6"/>
        <circle cx="23" cy="23" r="20" fill="#eb3d1f"/>
        <path d="M23 12 C19 18 16 22 16 26 a7 7 0 0 0 14 0 C30 22 27 18 23 12Z" fill="none" stroke="#fff" stroke-width="1.6"/>
      </svg>
      <div class="step__title">REFER FLOOD WATER AND<br>MOLD DAMAGE</div>
      <div class="step__body">Call, book online, or text us directly</div>
    </div>
    <div class="step step--two">
      <svg class="step__icon" viewBox="0 0 46 46" aria-hidden="true">
        <circle cx="23" cy="23" r="23" fill="#f8d3d4" opacity=".6"/>
        <circle cx="23" cy="23" r="20" fill="#eb3d1f"/>
        <rect x="15" y="12" width="16" height="21" rx="1.5" fill="none" stroke="#fff" stroke-width="1.5"/>
        <path d="M18 18h2M22 18h6M18 23h2M22 23h6M18 28h2M22 28h6" stroke="#fff" stroke-width="1.4"/>
      </svg>
      <div class="step__title">WE TAKE CARE OF<br>EVERYTHING</div>
      <div class="step__body">Free evaluations, insurance claims, and professional</div>
    </div>
    <div class="step step--three">
      <svg class="step__icon" viewBox="0 0 46 46" aria-hidden="true">
        <circle cx="23" cy="23" r="23" fill="#f8d3d4" opacity=".6"/>
        <circle cx="23" cy="23" r="20" fill="#eb3d1f"/>
        <circle cx="23" cy="23" r="11" fill="none" stroke="#fff" stroke-width="1.5"/>
        <path d="M18 23l3.5 3.5L28 19.5" fill="none" stroke="#fff" stroke-width="1.8"/>
      </svg>
      <div class="step__title">GET PAID FAST</div>
      <div class="step__body" style="margin-top:6px">$500 minimum or 10% of the invoice within 48 hours of final payment</div>
    </div>

    <svg style="position:absolute;left:0;top:264px" width="545" height="44" viewBox="0 0 545 44" aria-hidden="true">
      <polygon points="0,0 229,0 245,44 0,44" fill="#000"/>
      <polygon points="0,8 222,8 236,44 0,44" fill="#eb3d1f"/>
    </svg>
    <div class="tab-text tab-text--call">CALL TEXT OR BOOK ON-LINE</div>

    <div class="info-band">
      <svg class="contact-icon" style="top:22px" width="22" height="22" viewBox="0 0 24 24" aria-hidden="true">
        <path d="M6.6 10.8c1.4 2.8 3.8 5.1 6.6 6.6l2.2-2.2c.3-.3.7-.4 1-.2 1.1.4 2.3.6 3.6.6.6 0 1 .4 1 1V20c0 .6-.4 1-1 1C10.6 21 3 13.4 3 4c0-.6.4-1 1-1h3.5c.6 0 1 .4 1 1 0 1.3.2 2.5.6 3.6.1.3 0 .7-.2 1L6.6 10.8z" fill="#eb3d1f"/>
      </svg>
      <div class="contact contact--phone">555-014-2290</div>
      <svg class="contact-icon" style="top:63px" width="25" height="20" viewBox="0 0 25 20" aria-hidden="true">
        <rect x="0" y="0" width="25" height="20" rx="2.5" fill="#eb3d1f"/>
        <path d="M2 3l10.5 8L23 3" fill="none" stroke="#000" stroke-width="2"/>
      </svg>
      <div class="contact contact--web">HarborlineRestore.com</div>
      <div class="divider" style="left:354px"></div>
      <div class="brand" style="left:354px;width:191px;top:34px">
        <span class="brand__mark"></span>HARBORLINE<br>BUILDERS
      </div>
    </div>
  </section>

</div>
</body>
</html>
```